Home Page Concept For New Website (BookMyAdvisor)

We are creating a new website that allows students to schedule time to see their school counselors (bookmyadvisor.example). We need a concept for the home page. You will need to create one concept and provide a jpg image for us for review. The homepage needs to have at least a logon section, a Latest News section, a section for 3 Ads all 125x125 and some content for text where we describe the site. A menu will need to contain the following: Home, Pricing, Help and Contact Us.

You will need also need to create a design of the basic interior page template which should have a smaller banner, header, footer etc. This template will be used when we build the actual application and lots of space will be needed in the content area to draw controls such as textboxes, buttons, grids, etc in order to implement the application functionality when we code it.

We have no logo or color scheme so you are free to use your imagination as long as it looks professional.

Once we accept the design, you will need to give us a zip file containing all the artifacts including the .psd files, jpg images, and any fonts used, etc.
Updates

The customer has reviewed all the designs submitted so far and feels like most do not really convey that it is a scheduling site. They want all pictures removed because this will confuse students and students will think that the picture is their actual counselor. So remove the pictures of all the people and add illustrations, graphics, icons of some images that are related to scheduling like calendars, time, watches, etc. Fade images into the banners, or background etc. and be creative. Remember this site is for multiple schools to signup to use for scheduling their counselors so it needs to convey that function.

I sent this out before but I needed to repeat it for other designers... The customer has reviewed all the designs submitted so far and feels like most do not really convey that it is a scheduling site. They want all pictures removed because this will confuse students and students will think that the picture is their actual counselor. So remove the pictures of all the people and add illustrations, graphics, icons of some images that are related to scheduling like calendars, time, watches, etc. Fade images into the banners, or background etc. and be creative. Remember this site is for multiple schools to signup to use for scheduling their counselors so it needs to convey that function. Also several designers did not follow directions that clearly stated the home page had to include a login panel. The users of this system need to be able to login directly from this page. A login panel needs to contain the standard user name, password, login button, forgot my password link or button and maybe a signup link or button....nothing more. So please review your designs and update them accordingly. Thanks

Industry/Entity Type

School

Font styles to use
Sans Serif

Requirements
Should not have
• We don't have a logo or any pre-determined colors. We just need a clean professional design that fits pretty much on one page without a lot of scrolling. For example, the customer does NOT want a site like this..

https://hourplanix.example/

where you scroll for days with large multi-color panels.

```html
<!DOCTYPE html>
<html lang="en">
<head>
<meta charset="utf-8">
<title>BookMyAdvisor – Home</title>
<link href="https://fonts.googleapis.com/css2?family=Source+Sans+3:wght@400;600;700&display=swap" rel="stylesheet">
<style>
:root{
  --backdrop:#c9c9c9;
  --page:#ffffff;
  --ink:#1d1d1d;
  --body:#3a3a3a;
  --header:#000000;
  --accent:#dc4437;
  --accent-dark:#c9372c;
  --panel-grey:#e3e3e3;
  --navy:#1b2446;
  --icon-line:rgba(255,255,255,.55);
}
*{box-sizing:border-box;margin:0;padding:0}
html,body{width:946px;height:1200px;overflow:hidden}
body{
  position:relative;
  font-family:"Source Sans 3",sans-serif;
  color:var(--ink);
  background:radial-gradient(ellipse at center,#e6e6e6 0%,var(--backdrop) 100%);
}
.page{position:absolute;left:41px;top:32px;width:864px;height:1100px;background:var(--page);box-shadow:0 0 6px rgba(0,0,0,.18)}
.site-header{position:absolute;left:0;top:0;width:864px;height:58px;background:var(--header)}
.brand{position:absolute;left:16px;top:15px;font-size:24px;font-weight:400;color:var(--accent);letter-spacing:.2px}
.main-nav{position:absolute;right:0;top:10px;height:38px;display:flex}
.main-nav a{color:#fff;text-decoration:none;font-size:11.5px;line-height:38px;padding:0 11px;border-left:1px solid #3a3a3a}
.main-nav a:first-child{border-left:none}
.main-nav a:last-child{padding-right:61px}
.hero{position:absolute;left:0;top:58px;width:864px;height:389px;overflow:hidden;
  background:linear-gradient(100deg,#e9e4de 0%,#d9d2c6 30%,#8fa58e 55%,#6f8a72 75%,#c9bba9 100%)}
.hero-icons{position:absolute;left:0;top:0;width:864px;height:389px}
.hero-caption{position:absolute;left:19px;top:139px;width:296px;height:168px;background:rgba(255,255,255,.72);border:1px solid rgba(255,255,255,.9)}
.hero-caption h2{position:absolute;left:14px;top:20px;font-size:19.5px;font-weight:400;line-height:35px;color:#111}
.btn-red{position:absolute;left:14px;top:101px;width:110px;height:30px;background:var(--accent);color:#fff;font-size:9.5px;line-height:30px;text-align:center;border-radius:2px}
.dots{position:absolute;left:17px;top:141px;display:flex;gap:3px}
.dots span{width:9px;height:9px;border-radius:50%;background:var(--navy)}
.dots span:first-child{background:#fff;border:1.5px solid var(--navy)}
.welcome h1,.section-title{font-size:19.5px;font-weight:400;color:#111;position:absolute}
.welcome h1{left:32px;top:471px}
.copy{position:absolute;font-size:9.9px;line-height:17.6px;color:var(--body)}
.welcome .copy{left:32px;top:505px;width:720px}
.btn-outline{position:absolute;width:110px;height:30px;border:1px solid var(--navy);border-radius:3px;font-size:9.5px;line-height:28px;text-align:center;color:#111}
.login{position:absolute;left:31px;top:633px;width:361px;height:222px;
  background:linear-gradient(160deg,#d63b30 0%,#e24a3d 45%,#e8503f 60%,#dc4034 100%)}
.login h2{position:absolute;left:14px;top:6px;font-size:19.5px;font-weight:400;color:#fff}
.login .intro{position:absolute;left:16px;top:55px;font-size:10px;color:#fff}
.field-label{position:absolute;font-size:8.5px;color:#fff;text-align:right;width:70px}
.field{position:absolute;left:78px;width:157px;height:28px;border:1px solid #fff;background:var(--accent-dark);color:#f3d3cf;font-size:10px;line-height:26px;padding-left:5px}
.field.pw{color:#fff;letter-spacing:1px;font-size:11px}
.btn-login{position:absolute;left:247px;top:136px;width:75px;height:30px;background:#0e0e0e;border-radius:3px;color:#fff;font-weight:700;font-size:11px;line-height:30px;text-align:center;box-shadow:0 2px 3px rgba(0,0,0,.3)}
.remember{position:absolute;left:84px;top:176px;font-size:7.5px;color:#fff;display:flex;align-items:center;gap:5px}
.remember i{width:8px;height:8px;background:#eee;border:1px solid #999;display:block}
.forgot{position:absolute;left:167px;top:176px;font-size:7.5px;color:#fff;text-decoration:underline}
.news{position:absolute;left:392px;top:633px;width:445px;height:222px;background:var(--panel-grey)}
.news .divider{position:absolute;left:222px;top:0;width:1px;height:222px;background:#fff}
.news h2{position:absolute;left:17px;top:4px;font-size:19.5px;font-weight:400;color:#111}
.news-item{position:absolute;top:37px;width:187px}
.news-photo{width:187px;height:112px}
.news-date{font-size:9px;color:var(--accent);margin-top:7px}
.news-title{font-size:11px;font-weight:700;margin-top:5px;letter-spacing:.2px}
.news-text{font-size:8px;margin-top:6px;color:#222}
.news-text span{color:var(--accent)}
.ads{position:absolute;left:31px;top:943px;display:flex;gap:8px}
.ad{position:relative;width:93px;height:93px}
.ad span{position:absolute;left:0;bottom:0;width:100%;height:15px;background:rgba(0,0,0,.55);color:#fff;font-size:10px;line-height:15px;padding-left:6px}
.footer-rule{position:absolute;left:41px;top:1131px;width:864px;height:3px;background:#dedede}
.footer-nav{position:absolute;left:0;top:1148px;width:946px;text-align:center;font-size:9.3px;color:#111}
.copyright{position:absolute;left:0;top:1167px;width:946px;text-align:center;font-size:9.5px;color:var(--accent)}
</style>
</head>
<body>
<div class="page">
  <header class="site-header">
    <div class="brand">BookMyAdvisor</div>
    <nav class="main-nav">
      <a>Home</a><a>Pricing</a><a>Help</a><a>Counsellors</a><a>Contact Us</a>
    </nav>
  </header>

  <section class="hero" role="img" aria-label="Banner with a faded calendar and clock showing scheduling">
    <svg class="hero-icons" viewBox="0 0 864 389" aria-hidden="true">
      <g fill="none" stroke="var(--icon-line)" stroke-width="5" stroke-linecap="round">
        <circle cx="520" cy="200" r="120"/>
        <circle cx="520" cy="200" r="108" stroke-width="2"/>
        <line x1="520" y1="200" x2="520" y2="120"/>
        <line x1="520" y1="200" x2="578" y2="228"/>
        <g stroke-width="4">
          <line x1="520" y1="98" x2="520" y2="112"/>
          <line x1="520" y1="288" x2="520" y2="302"/>
          <line x1="418" y1="200" x2="432" y2="200"/>
          <line x1="608" y1="200" x2="622" y2="200"/>
        </g>
      </g>
      <circle cx="520" cy="200" r="7" fill="var(--icon-line)"/>
      <g fill="none" stroke="var(--icon-line)" stroke-width="4">
        <rect x="670" y="90" width="150" height="150" rx="8"/>
        <line x1="670" y1="128" x2="820" y2="128"/>
        <line x1="705" y1="78" x2="705" y2="100" stroke-linecap="round"/>
        <line x1="785" y1="78" x2="785" y2="100" stroke-linecap="round"/>
        <g stroke-width="2">
          <line x1="670" y1="156" x2="820" y2="156"/>
          <line x1="670" y1="184" x2="820" y2="184"/>
          <line x1="670" y1="212" x2="820" y2="212"/>
          <line x1="707" y1="128" x2="707" y2="240"/>
          <line x1="745" y1="128" x2="745" y2="240"/>
          <line x1="782" y1="128" x2="782" y2="240"/>
        </g>
        <polyline points="753,172 761,180 775,162" stroke="rgba(220,68,55,.8)" stroke-width="4" stroke-linecap="round" stroke-linejoin="round"/>
      </g>
      <rect x="670" y="90" width="150" height="38" rx="8" fill="rgba(220,68,55,.35)"/>
    </svg>
    <div class="hero-caption">
      <h2>Proin Gravida Nibh Velvelit<br>Auctor Etenean Sollicitudin</h2>
      <div class="btn-red">GET SCHEDULE TIME</div>
      <div class="dots"><span></span><span></span><span></span><span></span></div>
    </div>
  </section>

  <section class="welcome">
    <h1>Welcome</h1>
    <p class="copy">Proin gravida nibh vel velit auctor aliquet. Aenean sollicitudin, lorem quis bibendum auctor, nisi elit consequat ipsum, nec sagittis sem nibh id elit. Duis sed odio sit amet nibh vulputate cursus a sit amet mauris. Morbi accumsan ipsum velit. Nam nec tellus a odio tincidunt auctor a ornare odio. Sed non&nbsp; mauris vitae erat consequat auctor eu in elit. Class aptent taciti sociosqu ad litora torquent per conubia nostra, per inceptos himenaeos</p>
    <div class="btn-outline" style="left:31px;top:570px">CONTACT US NOW!</div>
  </section>

  <section class="login">
    <h2>Login</h2>
    <p class="intro">Lorem Ipsum is simply dummy text of roin gravida nibh vel velit auctor alique</p>
    <div class="field-label" style="left:0;top:109px">Email:</div>
    <div class="field" style="top:100px">enter email here</div>
    <div class="field-label" style="left:0;top:146px">Password:</div>
    <div class="field pw" style="top:137px">●●●●●●●●●●●</div>
    <div class="btn-login">LOGIN</div>
    <div class="remember"><i></i>Remember Me</div>
    <div class="forgot">Forgot password?</div>
  </section>

  <section class="news">
    <h2>Latest News</h2>
    <div class="divider"></div>
    <article class="news-item" style="left:17px">
      <div class="news-photo" role="img" aria-label="Photo of a teacher holding a course sign at a chalkboard" style="background:linear-gradient(135deg,#4a4f55,#7d7a80 55%,#c9b7c4)"></div>
      <div class="news-date">DEC 16, 2013</div>
      <div class="news-title">Lorem Ipsum Proin Gravida</div>
      <div class="news-text">Aenean sollicitudin, lorem quis&nbsp; <span>read more</span></div>
    </article>
    <article class="news-item" style="left:239px;top:36px">
      <div class="news-photo" role="img" aria-label="Photo of students working at desks in a classroom" style="background:linear-gradient(135deg,#b9b3ab,#6d6a66 50%,#9fa3a8)"></div>
      <div class="news-date" style="margin-top:6px">DEC 16, 2013</div>
      <div class="news-title">Lorem Ipsum Proin Gravida</div>
      <div class="news-text">Aenean sollicitudin, lorem quis&nbsp; <span>read more</span></div>
    </article>
  </section>

  <h2 class="section-title" style="left:61px;top:893px">Get Help +01 555 010 4477</h2>
  <div class="ads">
    <div class="ad" role="img" aria-label="Ad photo of students studying outdoors" style="background:linear-gradient(135deg,#9bb07a,#b45a5a)"><span>Ad here</span></div>
    <div class="ad" role="img" aria-label="Ad photo of a group of smiling students" style="background:linear-gradient(135deg,#6f7c5a,#c49a86)"><span>Ad here</span></div>
    <div class="ad" role="img" aria-label="Ad photo of students in a study group" style="background:linear-gradient(135deg,#8a7f7a,#d3b3b0)"><span>Ad here</span></div>
  </div>

  <h2 class="section-title" style="left:365px;top:893px">About Us</h2>
  <p class="copy" style="left:364px;top:934px;width:470px">Proin gravida nibh vel velit auctor aliquet. Aenean sollicitudin, lorem quis bibendum auctor, nisi elit consequat ipsum, nec sagittis sem nibh id elit. Duis sed odio sit amet nibh vulputate cursus a sit amet mauris. Morbi accumsan ipsum velit. Nam nec tellus a odio tincidunt auctor a ornare odio.</p>
  <div class="btn-outline" style="left:363px;top:1006px">READ MORE</div>
</div>

<div class="footer-rule"></div>
<nav class="footer-nav">Home&nbsp; | &nbsp;Pricing&nbsp; | &nbsp;Help&nbsp; | &nbsp;Counsellors&nbsp; | &nbsp;Contact Us</nav>
<p class="copyright">© 2014 site name All rights reserved</p>
</body>
</html>
```